Asian Pakistani: Wedding Invitation

Design a pakistani asian wedding invitation.
Islamic theme, with arabic text:

Text to be used:

Start with: bismillah and dua for marriage. (The Holy Quran chapter 25 verse 75 with arabic text and english translation below)

Mrs. Rukhsana Iqbal wife of (late) Mr. Nadeem Rauf Siddiqui
Cordially requests your company to grace the joyous occasion of the wedding of their beloved daughter
Sadia Siddiqui
Daughter of ( late) Mr Nadeem Rauf siddiqui
with
Imran Bashir
Son of Mr. Javed Bashir & Mrs Shaista Bashir

Insha’Allah on Thursday 29th August 2019 at Royal Orchid
12 Linden Crescent, Croydon
CR9 7TQ
Baraat Arrival 6:30

RSVP
Omar Siddiqui 07700 900412
Bilal Rehman 07700 900837
Shahzad Malik 07700 900265

Target Market(s)

Muslims

Font styles to use
Script

Colors

Designer to choose colors to be used in the design.

Requirements
Must have
• stylish calligraphy Arabic lettering of the dua requested above
• Size:
• Long 4" x 9.5"
Nice to have
• ottoman empire: Art theme

```html
<!DOCTYPE html>
<html lang="en">
<head>
<meta charset="utf-8">
<title>Wedding Invitation – Sadia &amp; Imran</title>
<link rel="stylesheet" href="https://fonts.googleapis.com/css2?family=Amiri:wght@400;700&family=Bodoni+Moda:ital,wght@0,400;0,700;1,700&family=Pinyon+Script&display=swap">
<style>
  :root {
    --gold: #d4961f;
    --gold-soft: #ebc37a;
    --ink: #2a2a2a;
    --paper: #ffffff;
    --pattern: #f2f2f2;
  }
  * { margin: 0; padding: 0; box-sizing: border-box; }
  html, body { width: 1200px; height: 2850px; overflow: hidden; background: var(--paper); }
  .invitation { position: relative; width: 1200px; height: 2850px; overflow: hidden;
    font-family: "Bodoni Moda", "Times New Roman", serif; color: var(--ink); }
  .abs { position: absolute; }
  .background-pattern { left: 0; top: 0; width: 1200px; height: 2850px;
    background: radial-gradient(circle at 50% 50%, #fbfbfb 0%, var(--pattern) 100%); }
  .ornament-band { left: 175px; width: 850px; height: 233px;
    background: radial-gradient(ellipse at 50% 100%, var(--gold) 0%, #e2ad4c 55%, rgba(226,173,76,0.25) 100%); }
  .ornament-band.top { top: 0; border-radius: 0 0 0 0; clip-path: ellipse(50% 100% at 50% 100%); }
  .ornament-band.bottom { top: 2617px; clip-path: ellipse(50% 100% at 50% 0%);
    background: radial-gradient(ellipse at 50% 0%, var(--gold) 0%, #e2ad4c 55%, rgba(226,173,76,0.25) 100%); }
  .card-frame { left: 110px; top: 273px; width: 980px; height: 2304px;
    background: var(--paper); border: 6px solid var(--gold); }
  .medallion { left: 487px; top: 282px; width: 226px; height: 133px;
    background: radial-gradient(ellipse at 50% 40%, var(--gold) 0%, #e4b560 70%, rgba(228,181,96,0) 100%);
    clip-path: ellipse(50% 50% at 50% 50%); }
  .side-ornament { top: 1960px; width: 178px; height: 305px;
    background: radial-gradient(ellipse at 50% 50%, var(--gold-soft) 0%, #f3d6a0 70%, rgba(243,214,160,0.3) 100%); }
  .side-ornament.left { left: 118px; clip-path: ellipse(100% 50% at 0% 50%); }
  .side-ornament.right { left: 904px; clip-path: ellipse(100% 50% at 100% 50%); }
  .center { left: 110px; width: 980px; text-align: center; }
  .arabic { font-family: "Amiri", serif; color: var(--gold); direction: rtl; }
  .bismillah { top: 490px; font-size: 56px; line-height: 1.2; }
  .verse-arabic { top: 740px; font-size: 64px; line-height: 80px; }
  .serif-bold { font-weight: 700; font-size: 27px; line-height: 38px; letter-spacing: 0.5px; }
  .bismillah-meaning { top: 595px; }
  .verse-meaning { top: 952px; }
  .verse-ref { top: 1040px; color: var(--gold); font-weight: 700; font-size: 23px; }
  .divider-vertical { left: 598px; top: 1100px; width: 3px; height: 97px; background: var(--gold-soft); }
  .hosts { top: 1238px; }
  .script-name { font-family: "Pinyon Script", cursive; color: var(--gold); font-size: 52px; line-height: 64px; }
  .bride { top: 1380px; }
  .groom { top: 1580px; }
  .parentage { font-weight: 700; font-size: 25px; }
  .bride-parentage { top: 1450px; }
  .groom-parentage { top: 1647px; }
  .with-rule { top: 1540px; height: 3px; background: var(--gold-soft); width: 359px; }
  .with-rule.left { left: 184px; } .with-rule.right { left: 657px; }
  .with-word { top: 1520px; font-style: italic; font-weight: 700; font-size: 26px; }
  .insha { top: 1720px; font-size: 40px; }
  .date-label { font-weight: 700; font-size: 30px; letter-spacing: 11px; line-height: 1; }
  .date-left { right: 733px; text-align: right; }
  .date-right { left: 736px; }
  .row-1 { top: 1826px; } .row-2 { top: 1877px; }
  .date-rule { top: 1810px; width: 3px; height: 110px; background: var(--ink); }
  .date-rule.left { left: 515px; } .date-rule.right { left: 684px; }
  .day-number { left: 516px; width: 170px; top: 1825px; text-align: center;
    font-weight: 700; font-size: 60px; letter-spacing: 12px; line-height: 1; }
  .venue-illustration { left: 465px; top: 2000px; width: 270px; height: 96px;
    background: linear-gradient(180deg, #f7e2b8 0%, var(--gold-soft) 100%); border: 2px solid var(--gold); }
  .venue { top: 2144px; font-weight: 700; font-size: 22px; line-height: 29.5px; letter-spacing: 4.5px; }
  .rsvp-rule { left: 184px; top: 2361px; width: 831px; height: 3px; background: var(--gold-soft); }
  .rsvp-title { left: 280px; top: 2422px; font-weight: 700; font-size: 70px; color: var(--gold); line-height: 1; }
  .rsvp-rule-vertical { left: 516px; top: 2413px; width: 3px; height: 108px; background: var(--gold-soft); }
  .rsvp-list { top: 2433px; font-weight: 700; font-size: 17.5px; line-height: 24px; }
  .rsvp-names { left: 563px; } .rsvp-phones { left: 774px; letter-spacing: 1px; }
</style>
</head>
<body>
<main class="invitation">
  <div class="abs background-pattern" role="img" aria-label="Faint grey arabesque pattern across the background"></div>
  <div class="abs ornament-band top" role="img" aria-label="Gold Ottoman-style mandala ornament, upper half"></div>
  <div class="abs ornament-band bottom" role="img" aria-label="Gold Ottoman-style mandala ornament, lower half"></div>

  <section class="abs card-frame"></section>
  <div class="abs medallion" role="img" aria-label="Small gold floral medallion ornament"></div>

  <p class="abs center arabic bismillah">بِسْمِ اللهِ الرَّحْمَنِ الرَّحِيْمِ</p>
  <p class="abs center serif-bold bismillah-meaning">In the name of Allah, the most Gracious,<br>most Merciful</p>

  <p class="abs center arabic verse-arabic">رَبَّنَا هَبْ لَنَا مِنْ أَزْوَٰجِنَا وَذُرِّيَّٰتِنَا قُرَّةَ<br>أَعْيُنٍ وَٱجْعَلْنَا لِلْمُتَّقِينَ إِمَامًا</p>
  <p class="abs center serif-bold verse-meaning">Our lord, grant us of our wives and children the delight<br>of our eyes, and make us a model of righteous</p>
  <p class="abs center verse-ref">Sura Al-Furqan:75</p>

  <div class="abs divider-vertical"></div>

  <p class="abs center serif-bold hosts">Mrs. Rukhsana Iqbal wife of (late) Mr. Nadeem Rauf Siddiqui<br>Cordially requests your company to grace the joyous occasion<br>of the wedding of their beloved daughter</p>

  <p class="abs center script-name bride">Sadia Siddiqui</p>
  <p class="abs center parentage bride-parentage">Daughter of (late) Mr Nadeem Rauf siddiqui</p>

  <div class="abs with-rule left"></div>
  <p class="abs center with-word">with</p>
  <div class="abs with-rule right"></div>

  <p class="abs center script-name groom">Imran Bashir</p>
  <p class="abs center parentage groom-parentage">Son of Mr. Javed Bashir &amp; Mrs Shaista Bashir</p>

  <p class="abs center arabic insha">إن شاء الله</p>

  <p class="abs date-label date-left row-1">THURSDAY</p>
  <p class="abs date-label date-left row-2">AUGUST</p>
  <div class="abs date-rule left"></div>
  <p class="abs day-number">29</p>
  <div class="abs date-rule right"></div>
  <p class="abs date-label date-right row-1">06.30 PM</p>
  <p class="abs date-label date-right row-2">2019</p>

  <div class="abs side-ornament left" role="img" aria-label="Pale gold mandala ornament, left half"></div>
  <div class="abs side-ornament right" role="img" aria-label="Pale gold mandala ornament, right half"></div>

  <div class="abs venue-illustration" role="img" aria-label="Gold line drawing of the venue building"></div>
  <p class="abs center venue">ROYAL ORCHID<br>12 LINDEN CRESCENT, CRODON<br>GRATER LONDON CR9 7TQ<br>BARAAT ARRIVAL 06:30 PM</p>

  <div class="abs rsvp-rule"></div>
  <p class="abs rsvp-title">RSVP</p>
  <div class="abs rsvp-rule-vertical"></div>
  <p class="abs rsvp-list rsvp-names">Omar Siddiqui<br>Bilal Rehman<br>Shahzad Malik</p>
  <p class="abs rsvp-list rsvp-phones">07700 900412<br>07700 900837<br>07700 900265</p>
</main>
</body>
</html>
```